Life Coach for Lawyers Business Card Design

Elegant, original, business card design for life coaching service for associate attorneys who work in big law and struggle with stress, overwhelm, and time management. Double sided design.

Target Market(s)

Women associate attorneys who work in big law and struggle with stress, overwhelm, and time management.

Industry/Entity Type

Life Coaching

Contact Information for Business Card

Marlene Quorthby
Life Coach
519.607.4431
brightcounselpath.net
marlene@brightcounselpath.net
@brightcounselpath (Instagram)

Font styles to use
Other font styles liked:
• Silver South font duo. See uploaded files.

Requirements
Must have
• Icons for phone, website, email, and Instagram instead of words. Specific colors used in my logo (171B2B, 421121, FFFFFF)
Nice to have
• Foil. Embossed. Feminine design.
Should not have
• Any colors other than those used in logo. See uploaded files.

```html
<!DOCTYPE html>
<html lang="en">
<head>
<meta charset="utf-8">
<title>Bright Counsel Path – Business Card</title>
<link rel="stylesheet" href="https://fonts.googleapis.com/css2?family=Playfair+Display:wght@400&family=Arimo:wght@400&display=swap">
<style>
  :root {
    --navy: #171B2B;
    --wine: #421121;
    --white: #FFFFFF;
    --ink: #1a1a1a;
    --page: #FFFFFF;
  }
  html, body {
    margin: 0;
    padding: 0;
    width: 1200px;
    height: 1200px;
    overflow: hidden;
    background: var(--page);
  }
  .sheet {
    position: relative;
    width: 1200px;
    height: 1200px;
  }
  .card {
    position: absolute;
    width: 756px;
    height: 464px;
    background: var(--white);
    overflow: hidden;
    outline: 1px solid #e6e6e6;
  }
  .card--front { left: 243px; top: 118px; }
  .card--back  { left: 245px; top: 638px; }
  .card__shapes {
    position: absolute;
    inset: 0;
    width: 756px;
    height: 464px;
  }
  .brand-name {
    position: absolute;
    left: 0;
    right: 0;
    text-align: center;
    font-family: "Playfair Display", Georgia, serif;
    font-weight: 400;
    letter-spacing: 1px;
    margin: 0;
  }
  .card--front .brand-name {
    top: 88px;
    font-size: 58px;
    color: var(--wine);
  }
  .card--back .brand-name {
    top: 78px;
    font-size: 48px;
    color: var(--ink);
  }
  .site-line {
    position: absolute;
    left: 0;
    right: 0;
    top: 408px;
    display: flex;
    align-items: center;
    justify-content: center;
    gap: 12px;
    font-family: "Arimo", Arial, sans-serif;
    font-size: 21px;
    color: var(--white);
  }
  .site-line__rule { width: 72px; height: 4px; }
  .person {
    position: absolute;
    right: 20px;
    top: 234px;
    text-align: right;
    font-family: "Arimo", Arial, sans-serif;
    color: var(--white);
  }
  .person__name { font-size: 32px; line-height: 38px; }
  .person__role { font-size: 22px; line-height: 28px; }
  .contacts {
    position: absolute;
    left: 43px;
    top: 302px;
    margin: 0;
    padding: 0;
    list-style: none;
    font-family: "Arimo", Arial, sans-serif;
    color: var(--white);
  }
  .contacts__item {
    display: flex;
    align-items: center;
    gap: 14px;
    height: 44px;
    font-size: 22px;
  }
  .contacts__item:first-child { font-size: 25px; }
  .contacts__icon { width: 32px; height: 32px; flex: none; }
</style>
</head>
<body>
<main class="sheet">

  <section class="card card--front" aria-label="Card front">
    <svg class="card__shapes" viewBox="0 0 756 464" aria-hidden="true">
      <path fill="var(--navy)" d="M0,282 C260,238 560,212 700,218 Q752,224 756,272 L756,464 L0,464 Z"/>
      <path fill="none" stroke="var(--white)" stroke-width="9" d="M0,344 C300,302 590,284 712,292 Q748,300 756,330"/>
    </svg>
    <h1 class="brand-name">Bright Counsel Path</h1>
    <div class="site-line">
      <svg class="site-line__rule" viewBox="0 0 72 4" aria-hidden="true"><path fill="var(--white)" d="M0,2 L72,0 L72,4 Z"/></svg>
      <span>www.brightcounselpath.net</span>
      <svg class="site-line__rule" viewBox="0 0 72 4" aria-hidden="true"><path fill="var(--white)" d="M0,0 L72,2 L0,4 Z"/></svg>
    </div>
  </section>

  <section class="card card--back" aria-label="Card back">
    <svg class="card__shapes" viewBox="0 0 756 464" aria-hidden="true">
      <path fill="var(--navy)" d="M0,0 L756,0 C730,30 660,42 520,38 C330,32 150,14 0,0 Z"/>
      <path fill="var(--navy)" d="M0,258 C290,200 600,174 756,184 L756,464 L0,464 Z"/>
    </svg>
    <h2 class="brand-name">Bright Counsel Path</h2>
    <div class="person">
      <div class="person__name">Marlene Quorthby</div>
      <div class="person__role">Life Coach</div>
    </div>
    <ul class="contacts">
      <li class="contacts__item">
        <svg class="contacts__icon" viewBox="0 0 32 32" aria-label="Phone">
          <circle cx="16" cy="16" r="15" fill="var(--white)"/>
          <path fill="var(--navy)" d="M11,8 l3,0 l1.5,4 l-2,1.5 q1.5,3.5 4.5,5 l1.5,-2 l4,1.5 l0,3 q-1,2 -3,2 q-6,-0.5 -10.5,-7 q-2,-3.5 -1.5,-6 q0.5,-2 2.5,-2 z"/>
        </svg>
        <span>519.607.4431</span>
      </li>
      <li class="contacts__item">
        <svg class="contacts__icon" viewBox="0 0 32 32" aria-label="Email">
          <circle cx="16" cy="16" r="15" fill="var(--white)"/>
          <rect x="8.5" y="11" width="15" height="10" fill="none" stroke="var(--navy)" stroke-width="1.6"/>
          <path fill="none" stroke="var(--navy)" stroke-width="1.6" d="M8.5,11 L16,17 L23.5,11"/>
        </svg>
        <span>marlene@brightcounselpath.net</span>
      </li>
      <li class="contacts__item">
        <svg class="contacts__icon" viewBox="0 0 32 32" aria-label="Website">
          <circle cx="16" cy="16" r="15" fill="var(--white)"/>
          <circle cx="16" cy="16" r="8" fill="none" stroke="var(--navy)" stroke-width="1.6"/>
          <ellipse cx="16" cy="16" rx="3.5" ry="8" fill="none" stroke="var(--navy)" stroke-width="1.4"/>
          <path fill="none" stroke="var(--navy)" stroke-width="1.4" d="M8,16 L24,16"/>
        </svg>
        <span>www.brightcounselpath.net</span>
      </li>
    </ul>
  </section>

</main>
</body>
</html>
```